Business cards for a tribute and obituary website

Our website is called Tribute Lantern.

It is a special place online for people to remember their loved ones who have passed away, through obituaries and tributes. Friends and family can also convey their condolences on the deceased's memorial page. Celebrating the life of the deceased and remembering their legacy is very important to us – death should not be just about grieving.

We would like the card to look tasteful and modern. The design should ideally not have colours that are too bright. The logo and website URL, www.tributelantern.example should be visible on the front of the card, with our slogan "Celebrating a life passed" on the back.

The design should communicate our purpose – remembering loved ones who have passed – and also a lighter tone of celebrating life. It should not look like a funeral director's card!

Our logo has been attached. Looking forward to some beautiful designs! Get creative :)
Updates

Project Deadline Extended
Reason: Thank you all for your designs. The rest of my team and I have not reached a decision on which design to select and I am collecting feedback from them. I will provide feedback for any changes that need to be made soon. It would be great if we could see more original designs and in more colours! We will definitely select a design by this deadline.

Industry/Entity Type

Business

Contact Information for Business Card

Wendy Lumb
Project Manager
614772390
wendylumb@tributelantern.example

Font styles to use
Serif
Sans Serif

Requirements
Must have
• Logo and website address (www.tributelantern.example) on the front.
Nice to have
• Hi designers! It would be nice to see alternative colours – feel free to try out colours that are tasteful and subtle. The colour of the business card does not have to be the same as the logo.
• We would also like to see the logo used in different ways, perhaps a glossy or embossed finish. The card should look stylish.

```html
<!DOCTYPE html>
<html lang="en">
<head>
<meta charset="utf-8">
<title>Tribute Lantern – Business Cards</title>
<link href="https://fonts.googleapis.com/css2?family=Roboto+Slab:wght@500;700&family=Mulish:wght@400&display=swap" rel="stylesheet">
<style>
  :root {
    --page-bg: #e4e4e4;
    --card-navy: #082946;
    --ink-white: #ffffff;
    --accent-blue: #4fa3dc;
    --rule-grey: #7d8fa3;
  }
  * { margin: 0; padding: 0; box-sizing: border-box; }
  html, body { width: 1189px; height: 1200px; overflow: hidden; }
  body { background: var(--page-bg); position: relative; color: var(--ink-white); }

  .card {
    position: absolute;
    left: 171px;
    width: 856px;
    height: 487px;
    background: var(--card-navy);
    border-radius: 24px;
  }
  .card--front { top: 68px; }
  .card--back { top: 627px; }

  .brand-mark {
    position: absolute;
    border-radius: 50%;
    border: 14px solid var(--ink-white);
  }
  .brand-name {
    position: absolute;
    font-family: "Roboto Slab", serif;
    font-weight: 700;
    color: var(--ink-white);
  }

  /* front */
  .card--front .brand-mark { left: 168px; top: 162px; width: 150px; height: 150px; }
  .card--front .brand-name { left: 355px; top: 140px; font-size: 66px; line-height: 70px; }
  .tagline {
    position: absolute; left: 356px; top: 289px;
    font-family: "Roboto Slab", serif; font-weight: 500;
    font-size: 25px; color: var(--accent-blue);
  }
  .front-url {
    position: absolute; left: 0; right: 0; top: 372px;
    display: flex; align-items: center; justify-content: center; gap: 20px;
    font-family: "Roboto Slab", serif; font-weight: 500; font-size: 22px;
  }
  .front-url .rule { width: 86px; height: 1px; background: var(--rule-grey); }

  /* back */
  .card--back .brand-mark { left: 100px; top: 90px; width: 180px; height: 180px; }
  .card--back .brand-name {
    left: 40px; width: 300px; top: 303px; text-align: center;
    font-size: 46px; line-height: 46px;
  }
  .divider { position: absolute; left: 372px; top: 68px; width: 2px; height: 350px; background: var(--ink-white); }
  .person { position: absolute; left: 429px; top: 102px; }
  .person-name { font-family: "Roboto Slab", serif; font-weight: 700; font-size: 43px; line-height: 46px; }
  .person-role { font-family: "Mulish", sans-serif; font-size: 21px; line-height: 22px; }
  .contact-list { position: absolute; left: 429px; top: 277px; list-style: none; }
  .contact-list li {
    display: flex; align-items: center; gap: 12px; height: 37px;
    font-family: "Mulish", sans-serif; font-size: 21px;
  }
  .contact-icon { width: 27px; height: 27px; flex: none; }
</style>
</head>
<body>

<section class="card card--front">
  <span class="brand-mark"></span>
  <h1 class="brand-name">Tribute<br>Lantern</h1>
  <p class="tagline">Celebrating a life passed</p>
  <p class="front-url"><span class="rule"></span>www.tributelantern.example<span class="rule"></span></p>
</section>

<section class="card card--back">
  <span class="brand-mark"></span>
  <h2 class="brand-name">Tribute<br>Lantern</h2>
  <span class="divider"></span>
  <div class="person">
    <p class="person-name">Wendy Lumb</p>
    <p class="person-role">Project Manager</p>
  </div>
  <ul class="contact-list">
    <li>
      <svg class="contact-icon" viewBox="0 0 27 27" aria-hidden="true">
        <rect width="27" height="27" rx="5" fill="#fff"/>
        <path d="M9 6c-2 1-3 3-2 6 1 4 4 8 8 10 2 1 4 0 5-2l-3-3-2 2c-2-1-4-4-5-6l2-2z" fill="#082946"/>
      </svg>614772390
    </li>
    <li>
      <svg class="contact-icon" viewBox="0 0 27 27" aria-hidden="true">
        <rect width="27" height="27" rx="5" fill="#fff"/>
        <rect x="5" y="8" width="17" height="12" fill="none" stroke="#082946" stroke-width="1.6"/>
        <path d="M5 8l8.5 7L22 8M5 20l6-6M22 20l-6-6" fill="none" stroke="#082946" stroke-width="1.6"/>
      </svg>wendylumb@tributelantern.example
    </li>
    <li>
      <svg class="contact-icon" viewBox="0 0 27 27" aria-hidden="true">
        <rect width="27" height="27" rx="5" fill="#fff"/>
        <g fill="none" stroke="#082946" stroke-width="1.4">
          <circle cx="13.5" cy="13.5" r="8"/>
          <ellipse cx="13.5" cy="13.5" rx="3.5" ry="8"/>
          <path d="M5.5 13.5h16M7 9h13M7 18h13"/>
        </g>
      </svg>www.tributelantern.example
    </li>
  </ul>
</section>

</body>
</html>
```